Healthcare patient advocacy company needs banner for conference booth

We need a banner to hang behind us in our booth at conferences. I would like something that prominently features our company name - brovint LLC. And also includes the following language: No employee should face medical debt alone. No Plan should be unrepresented. Expert advocacy and legal support from first bill to final resolution. The colors we use for our other materials are HEX 002C45, FECC73, 00C6CF, E0D5B9, 004C66. And the font is Epilogue. I would welcome some graphics, but no scales of justice or dollar bills or anything like that. I'm attaching some materials so you can see one of our brochures.

Target Market(s)

B2B - health insurers, third-party health care administrators, cost-containment companies

Industry/Entity Type

Healthcare Advocacy

Requirements
Must have
• Name prominently displayed and taglines in project description.
Nice to have
• I would like something easy to read and eye-catching that is not overly complicated or cutsey.
Should not have
• Scales of justice or dollar signs.

```html
<!DOCTYPE html>
<html lang="en">
<head>
<meta charset="utf-8">
<title>brovint LLC – Booth Banner</title>
<link rel="stylesheet" href="https://fonts.googleapis.com/css2?family=Epilogue:wght@400;500;700;800&family=Barlow+Semi+Condensed:wght@600;700&display=swap">
<style>
  :root {
    --navy: #002C45;
    --navy-deep: #021a2a;
    --navy-mid: #004C66;
    --gold: #FECC73;
    --teal: #00C6CF;
    --sand: #E0D5B9;
    --white: #ffffff;
    --stage: #b3b3b3;
  }
  * { margin: 0; padding: 0; box-sizing: border-box; }
  html, body {
    width: 706px; height: 1200px; overflow: hidden;
    background: var(--stage);
  }
  .banner {
    position: absolute;
    left: 23px; top: 336px;
    width: 660px; height: 528px;
    background: var(--white);
    overflow: hidden;
  }
  .top-band {
    position: absolute; left: 0; top: 0; width: 100%; height: 32px;
    background: radial-gradient(ellipse 40% 140% at 50% 0%, #0a4b7a 0%, var(--navy) 55%, var(--navy-deep) 100%);
  }
  .name-band {
    position: absolute; left: 0; top: 32px; width: 100%; height: 57px;
    background: linear-gradient(90deg, #d6d6d8 0%, #ffffff 22%, #ffffff 78%, #d2d2d4 100%);
    display: flex; align-items: center; justify-content: center;
  }
  .company-name {
    font-family: "Epilogue", sans-serif;
    font-weight: 800;
    font-size: 36px;
    letter-spacing: -0.5px;
    color: var(--navy-deep);
    line-height: 1;
    padding-top: 4px;
  }
  .message {
    position: absolute; left: 0; top: 89px; width: 100%; height: 211px;
    background: linear-gradient(180deg, var(--navy) 0%, #031f33 50%, var(--navy-deep) 100%);
    text-align: center;
    padding-top: 24px;
  }
  .headline {
    font-family: "Barlow Semi Condensed", sans-serif;
    font-weight: 700;
    font-size: 39px;
    line-height: 38px;
    color: var(--white);
  }
  .subhead {
    margin-top: 4px;
    font-family: "Barlow Semi Condensed", sans-serif;
    font-weight: 700;
    font-size: 27px;
    line-height: 30px;
    color: var(--gold);
  }
  .body-copy {
    margin-top: 6px;
    font-family: "Epilogue", sans-serif;
    font-weight: 400;
    font-size: 16px;
    line-height: 20px;
    color: var(--white);
  }
  .divider {
    position: absolute; left: 0; top: 300px; width: 100%; height: 7px;
    background: #0b3a5e;
  }
  .team-photo {
    position: absolute; left: 0; top: 307px; width: 100%; height: 190px;
    background: linear-gradient(90deg, #1b2f40 0%, #2a4356 30%, #5a5a5c 55%, #8a6a45 75%, #6b5034 100%);
  }
  .footer-shape {
    position: absolute; left: 0; top: 460px; width: 660px; height: 68px;
  }
  .url {
    position: absolute; left: 180px; top: 474px; width: 300px;
    text-align: center;
    font-family: "Epilogue", sans-serif;
    font-size: 19px;
    font-weight: 500;
    color: var(--navy-mid);
  }
  .url .domain { color: var(--teal); font-weight: 700; }
</style>
</head>
<body>
  <section class="banner">
    <div class="top-band"></div>
    <header class="name-band">
      <h1 class="company-name">brovint LLC</h1>
    </header>
    <div class="message">
      <h2 class="headline">NO EMPLOYEE SHOULD FACE<br>MEDICAL DEBT ALONE.</h2>
      <p class="subhead">NO PLAN SHOULD BE UNREPRESENTED</p>
      <p class="body-copy">Expert advocacy and legal support from first bill<br>to final resolution.</p>
    </div>
    <div class="divider"></div>
    <div class="team-photo" role="img" aria-label="Photo of a business team collaborating around a laptop in a modern office"></div>
    <svg class="footer-shape" viewBox="0 0 660 68" aria-hidden="true">
      <rect x="0" y="37" width="660" height="16" fill="#021a2a"/>
      <rect x="0" y="53" width="660" height="15" fill="#ffffff"/>
      <path d="M150 53 C170 53 172 40 178 25 C184 10 190 7 205 7 H455 C470 7 476 10 482 25 C488 40 490 53 510 53 Z" fill="#ffffff"/>
    </svg>
    <p class="url">www.<span class="domain">brovinthealth</span>.com</p>
  </section>
</body>
</html>
```